Small business providing disability support care requires services promotional poster

We need a digital poster to promote our services to PSAF service providers. We deliver individualised support to people living with disabilities of all ages. (Examples -Physical, intellectual, autism, hearing/vision impaired).We need the poster to highlight the services we offer - attached for convenience + group support, holiday support, camping and outdoor activities. We already have our own logo, we would like the colour theme to fit the logo aesthetic - attached. The design should communicate respect, holistic and collaborative care, fun and inclusivity.
RW Care Supports ( former name - Talvoro Vigour & Motion)

Target Market(s)

PSAF service providers (ROT, Support Coordinators, PSAF participants, Support agencies)

Industry/Entity Type

Community Services

Font styles to use
Sans Serif

Requirements
Must have
• Person centred positive imagery and language
Should not have
• Typical wheelchair or 'disabled' visuals, no puzzle pieces. Not too bright or busy - sensory overload

```html
<!DOCTYPE html>
<html lang="en">
<head>
<meta charset="utf-8">
<title>RW Care Supports – Our Services</title>
<link href="https://fonts.googleapis.com/css2?family=Barlow+Condensed:wght@400;700&family=Roboto:wght@400;700&family=Open+Sans:wght@700&display=swap" rel="stylesheet">
<style>
  :root {
    --rose-deep: #e3c3b8;
    --rose-soft: #f3dbd6;
    --rose-pale: #f3e3df;
    --ink: #111111;
    --icon-tone: rgba(17, 17, 17, 0.07);
    --photo-warm: #d9a982;
    --photo-light: #f6eee6;
    --photo-cool: #dfe4ee;
  }
  * { box-sizing: border-box; margin: 0; padding: 0; }
  html, body { width: 800px; height: 1200px; overflow: hidden; background: #fff; }
  .poster {
    position: relative; width: 800px; height: 1200px; overflow: hidden;
    font-family: "Barlow Condensed", sans-serif; color: var(--ink);
  }
  .panel { position: absolute; padding: 26px 20px 0 31px; }
  .panel--right { padding-left: 30px; }
  .bg-deep { background: var(--rose-deep); }
  .bg-soft { background: var(--rose-soft); }
  .bg-pale { background: var(--rose-pale); }

  .service-title { font-size: 16.5px; font-weight: 700; margin-bottom: 11px; line-height: 22px; }
  .service-title--light { font-weight: 400; font-size: 17px; }
  .service-lead { font-size: 13.8px; margin-bottom: 8px; line-height: 21.5px; }
  .service-list { list-style: none; font-size: 14px; line-height: 21.5px; }
  .service-list li { position: relative; padding-left: 19px; }
  .service-list li::before { content: "•"; position: absolute; left: 6px; font-size: 10px; }
  .service-list--tight { line-height: 19.5px; }
  .panel--small .service-lead { font-size: 12.8px; }
  .panel--small .service-list { font-size: 12.6px; }
  .panel--training .service-lead { font-size: 13.3px; }

  .intro { padding: 30px 20px 0 31px; font-family: "Roboto", sans-serif; }
  .intro-text { font-size: 13.6px; line-height: 26.5px; }
  .intro-tagline { font-size: 14px; font-weight: 700; margin-top: 7px; }

  .icon-slot { position: absolute; background: var(--icon-tone); border-radius: 6px; }

  .photo {
    position: absolute; left: 0; top: 378px; width: 800px; height: 224px;
    background: linear-gradient(100deg, #b9a27c 0%, var(--photo-warm) 25%, #e7c6a6 45%, var(--photo-light) 62%, var(--photo-cool) 85%, #c9d0e0 100%);
  }
  .brand-name {
    position: absolute; left: 31px; top: 512px;
    font-family: "Barlow Condensed", sans-serif; font-weight: 700; font-size: 20px; color: var(--ink);
  }
  .contact { position: absolute; right: 32px; text-align: right; font-family: "Open Sans", sans-serif; font-weight: 700; color: var(--ink); line-height: 28px; }
  .contact-phone { top: 516px; font-size: 20.5px; }
  .contact-email { top: 551px; font-size: 19.5px; }
</style>
</head>
<body>
<main class="poster">

  <section class="panel intro bg-deep" style="left:0;top:0;width:400px;height:169px;">
    <p class="intro-text">Delivering person centered supports to individuals living with disabilities to support, empower and build the capacity of every person aligned with RW Care Supports.</p>
    <p class="intro-tagline">Delivering honest, holistic and reliable care.</p>
  </section>

  <section class="panel panel--right bg-pale" style="left:400px;top:0;width:400px;height:169px;">
    <h2 class="service-title">Help Around the House</h2>
    <p class="service-lead">Various forms of day to day assistance around the house:</p>
    <ul class="service-list">
      <li>Assisting with yard care and home maintenance</li>
      <li>Cleaning, cooking and washing</li>
      <li>Home office duties</li>
    </ul>
  </section>

  <section class="panel panel--small bg-soft" style="left:0;top:169px;width:400px;height:209px;">
    <h2 class="service-title">Individual Empowerment</h2>
    <p class="service-lead">Support to build capacity to become more independent:</p>
    <ul class="service-list">
      <li>Assistance with effective decision making</li>
      <li>Assistance with advocacy and discussions with Service Providers at the request of the participant</li>
      <li>Ensuring choice and control is being uphelp by participant</li>
      <li>Supporting the participant to understand choices with informed consent</li>
    </ul>
  </section>

  <section class="panel panel--right bg-deep" style="left:400px;top:169px;width:400px;height:209px;">
    <h2 class="service-title">In-Home Care</h2>
    <p class="service-lead">Support with routines around school, work and medication:</p>
    <ul class="service-list">
      <li>Supervising or assisting with meal preparation</li>
      <li>Help with morning and evening routines</li>
      <li>Assistance with budgeting and paying bills</li>
      <li>Assistance with Independent Living Skills</li>
    </ul>
  </section>

  <div class="photo" role="img" aria-label="Photo of several people's hands stacked together in a gesture of teamwork"></div>
  <p class="brand-name">RW Care Supports</p>
  <p class="contact contact-phone">0400 118 246</p>
  <p class="contact contact-email">hello@rwcaresupports.com.au</p>

  <section class="panel bg-deep" style="left:0;top:602px;width:400px;height:190px;">
    <h2 class="service-title">Education and Employment</h2>
    <p class="service-lead">Learning and developing employable skills.</p>
    <ul class="service-list">
      <li>Developing skills in School, University and Work</li>
      <li>Assistance with completing assignments</li>
      <li>Transition from school to further learning, work experience or work</li>
    </ul>
  </section>

  <section class="panel panel--right bg-pale" style="left:400px;top:602px;width:400px;height:170px;">
    <h2 class="service-title">Personal Care</h2>
    <p class="service-lead">Assistance with day to day health and hygiene care:</p>
    <ul class="service-list">
      <li>Showering</li>
      <li>Bathroom assistance</li>
      <li>Meal assistance</li>
    </ul>
  </section>

  <section class="panel bg-pale" style="left:0;top:792px;width:400px;height:230px;">
    <h2 class="service-title">Transport</h2>
    <p class="service-lead">Assistance to get from A to B:</p>
    <ul class="service-list">
      <li>Getting to appointments and therapy supports</li>
      <li>Day to day activities</li>
      <li>Transport to education or work</li>
      <li>Travel Training to build individuals capacity to independently travel</li>
      <li>Driving Hours for participants wanting to increase their current learner permit hours</li>
    </ul>
  </section>

  <section class="panel panel--right bg-soft" style="left:400px;top:772px;width:400px;height:194px;">
    <h2 class="service-title">Out and About</h2>
    <p class="service-lead">Assistance with accessing the community:</p>
    <ul class="service-list service-list--tight">
      <li>Support in taking a class to learn new skills</li>
      <li>Volunteering in the community</li>
      <li>Going to social activities</li>
      <li>Sport and recreational activities (camping, fishing, bush walking and more)</li>
    </ul>
  </section>

  <section class="panel bg-soft" style="left:0;top:1022px;width:400px;height:178px;">
    <h2 class="service-title">Respite Care</h2>
    <p class="service-lead">Support in Direct Support Worker’s home:</p>
    <ul class="service-list">
      <li>Provide support in your home</li>
      <li>Overnight Stay</li>
      <li>Support with night and morning routine</li>
    </ul>
  </section>

  <section class="panel panel--right panel--training bg-deep" style="left:400px;top:966px;width:400px;height:234px;padding-right:8px;">
    <h2 class="service-title service-title--light">Personal Training</h2>
    <p class="service-lead">Improving Fitness with participants. (I can not train participants with major health concerns or complex physical therapy needs unless instructed by a physiotherapist or their Health Care Professional):</p>
    <ul class="service-list">
      <li>Resistance training</li>
      <li>Powerlifting Training</li>
      <li>Boxing</li>
      <li>General sport practice</li>
    </ul>
  </section>

  <div class="icon-slot" role="img" aria-label="Line icon of a clean house" style="left:714px;top:84px;width:68px;height:68px;"></div>
  <div class="icon-slot" role="img" aria-label="Line icon of a light bulb" style="left:322px;top:189px;width:64px;height:72px;"></div>
  <div class="icon-slot" role="img" aria-label="Line icon of a hand holding a house" style="left:697px;top:270px;width:82px;height:82px;"></div>
  <div class="icon-slot" role="img" aria-label="Line icon of a graduation cap" style="left:298px;top:633px;width:80px;height:66px;"></div>
  <div class="icon-slot" role="img" aria-label="Line icon of a bathtub with bubbles" style="left:699px;top:689px;width:70px;height:66px;"></div>
  <div class="icon-slot" role="img" aria-label="Line icon of a car with a return arrow" style="left:286px;top:824px;width:80px;height:56px;"></div>
  <div class="icon-slot" role="img" aria-label="Line icon of a person with a speech bubble" style="left:699px;top:811px;width:68px;height:80px;"></div>
  <div class="icon-slot" role="img" aria-label="Line icon of sun and moon for day and night" style="left:288px;top:1077px;width:80px;height:80px;"></div>
  <div class="icon-slot" role="img" aria-label="Line icon of a trainer lifting a dumbbell" style="left:696px;top:1100px;width:54px;height:84px;"></div>

</main>
</body>
</html>
```